Halvik Partners Building Business Cards

We need a business card that reflects our business as "Solar Experts" in San Diego. Browse our website www.halvikpartners.example our License needs to be displayed as "CSLB# 4871306" our phone number is (619) 482-5537

Save thousands on your electric bills and increase the value of your home while helping to protect the environment. Our solar installation experts will help you design the system that's right for you, using only the highest quality equipment that will look great and give you ideal performance. Our goal is to make you energy independent, and get your electric bill to 0.

Paul Ostrander
(619) 482-5537
paul@halvikpartners.example

Target Market(s)

Home owners in san diego looking for solar

Industry/Entity Type

Solar Energy

Contact Information for Business Card

Paul Ostrander
(619) 482-5537
paul@halvikpartners.example

Font styles to use
Other font styles liked:
• Use our logo font

Requirements
Must have
• License needs to be displayed as "CSLB# 4871306" our phone number is (619) 482-5537
Nice to have
• Real images of rooftop home solar in san diego
Should not have
• our business address

```html
<!DOCTYPE html>
<html lang="en">
<head>
<meta charset="utf-8">
<title>Halvik Partners Building – Business Cards</title>
<link href="https://fonts.googleapis.com/css2?family=Cinzel:wght@500;600&family=Roboto:wght@400;700&family=Libre+Baskerville:ital@1&display=swap" rel="stylesheet">
<style>
  :root {
    --navy: #1f3d7a;
    --navy-deep: #1b3670;
    --sun: #f5ac00;
    --ink: #555b66;
    --rule: #c9ccd2;
    --paper: #ffffff;
    --backdrop: #e4e5e8;
  }
  html, body {
    margin: 0;
    width: 1200px;
    height: 1000px;
    overflow: hidden;
    background: var(--backdrop);
  }
  .canvas {
    position: relative;
    width: 1200px;
    height: 1000px;
  }
  .card {
    position: absolute;
    left: 220px;
    width: 760px;
    box-shadow: 0 4px 12px rgba(0,0,0,.25);
  }
  /* Front */
  .card-front {
    top: 50px;
    height: 433px;
    background: var(--navy);
    color: var(--paper);
  }
  .front-brand {
    position: absolute;
    top: 200px;
    left: 0;
    width: 100%;
    display: flex;
    justify-content: center;
    align-items: center;
    gap: 16px;
    transform: translateY(-50%);
  }
  .brand-dot {
    width: 20px;
    height: 20px;
    border-radius: 50%;
    background: var(--sun);
    flex: none;
  }
  .brand-name {
    font-family: "Roboto", Arial, sans-serif;
    font-weight: 700;
    font-size: 50px;
    letter-spacing: -0.5px;
    color: var(--paper);
    line-height: 1;
    white-space: nowrap;
  }
  .tagline {
    position: absolute;
    top: 370px;
    left: 0;
    width: 100%;
    text-align: center;
    font-family: "Libre Baskerville", "Times New Roman", serif;
    font-style: italic;
    font-size: 25px;
    line-height: 1;
    margin: 0;
    transform: translateY(-50%);
  }
  /* Back */
  .card-back {
    top: 524px;
    height: 436px;
    background: var(--paper);
    overflow: hidden;
  }
  .back-brand {
    position: absolute;
    left: 45px;
    top: 216px;
    width: 360px;
    display: flex;
    align-items: center;
    gap: 12px;
    transform: translateY(-50%);
  }
  .back-brand .brand-square {
    width: 18px;
    height: 18px;
    background: var(--navy);
    flex: none;
  }
  .back-brand .brand-name {
    color: var(--navy);
    font-size: 27px;
    letter-spacing: -0.3px;
  }
  .divider {
    position: absolute;
    left: 415px;
    top: 152px;
    width: 1px;
    height: 150px;
    background: var(--rule);
  }
  .contact-block {
    position: absolute;
    left: 438px;
    top: 148px;
  }
  .person-name {
    font-family: "Cinzel", Georgia, serif;
    font-weight: 600;
    font-size: 24px;
    line-height: 28px;
    color: var(--navy);
    margin: 0;
    letter-spacing: .5px;
  }
  .person-role {
    font-family: "Roboto", Arial, sans-serif;
    font-size: 17px;
    line-height: 22px;
    color: var(--ink);
    margin: 0 0 17px;
  }
  .contact-list {
    list-style: none;
    margin: 0;
    padding: 0;
    font-family: "Roboto", Arial, sans-serif;
    font-size: 17px;
    color: var(--ink);
  }
  .contact-list li {
    display: flex;
    align-items: center;
    gap: 7px;
    height: 24px;
    white-space: nowrap;
  }
  .contact-list svg {
    width: 13px;
    height: 13px;
    fill: var(--sun);
    flex: none;
  }
  .license-mark {
    width: 13px;
    height: 13px;
    flex: none;
  }
  .bottom-band {
    position: absolute;
    bottom: 0;
    left: 0;
    width: 100%;
    height: 16px;
    display: flex;
    gap: 3px;
  }
  .band-navy { width: 437px; background: var(--navy-deep); }
  .band-sun { flex: 1; background: var(--sun); }
</style>
</head>
<body>
<main class="canvas">
  <section class="card card-front">
    <div class="front-brand">
      <span class="brand-dot"></span>
      <span class="brand-name">Halvik Partners Building</span>
    </div>
    <p class="tagline">The Solar Experts</p>
  </section>

  <section class="card card-back">
    <div class="back-brand">
      <span class="brand-square"></span>
      <span class="brand-name">Halvik Partners Building</span>
    </div>
    <div class="divider"></div>
    <div class="contact-block">
      <h2 class="person-name">Paul Ostrander</h2>
      <p class="person-role">President</p>
      <ul class="contact-list">
        <li>
          <svg viewBox="0 0 16 16" aria-hidden="true"><path d="M3 1l3 3-1.5 2c1 2 3 4 5 5l2-1.5 3 3-2 2C6 14 2 10 1 3z"/></svg>
          (619) 482-5537
        </li>
        <li>
          <svg viewBox="0 0 16 16" aria-hidden="true"><path d="M1 3h14v10H1z M1 3l7 6 7-6" stroke="#fff" stroke-width="1.2"/></svg>
          paul@halvikpartners.example
        </li>
        <li>
          <svg viewBox="0 0 16 16" aria-hidden="true"><circle cx="8" cy="8" r="7"/><path d="M1 8h14M8 1c-3 3-3 11 0 14M8 1c3 3 3 11 0 14" stroke="#fff" stroke-width="1" fill="none"/></svg>
          www.halvikpartners.example
        </li>
        <li>
          <svg viewBox="0 0 16 16" aria-hidden="true"><path d="M2 2h12v12H2z"/><path d="M5 8l2 2 4-4" stroke="#fff" stroke-width="1.6" fill="none"/></svg>
          CSLB# 4871306
        </li>
      </ul>
    </div>
    <div class="bottom-band">
      <span class="band-navy"></span>
      <span class="band-sun"></span>
    </div>
  </section>
</main>
</body>
</html>
```